Business Card: RW Office Partners - Your tidy answer finder

Business Name: RW Office Partners
Website: www.rwofficepartners.com.au
Email: marisol@rwofficepartners.com.au
Mobile: 61 487 902 346
Facebook: @rwofficepartners
Instrgram: @rwofficepartners

Brading Colours:
HEX
#986474
#ddccd3
#7a8498
#c9d8e4
#000000
#ffffff

Tag Line: Your organised problem solver

Link to DRAFT website:
https://helpdeskhub.sitebuilderx.com/rw-office-partners

About Page from the website:
My name is Marisol Bramwell, and I would love to assist you to become more productive in your day to day and achieve your business and personal goals.
My mission is to give you time, time to work on the important tasks of your business or to be able to spend more time with your family. I will take on the tasks you don’t have time for, don’t know well or simply don’t like to do.
I have an extensive background in Administration, Tender Coordination, Document Control, WHS and Quality Management working primarily in the Construction, Mining and Corporate World.
I am passionate about being organised, having order and making things in your life (and mine) easier! I love to watch something unfold and grow into something amazing! I am known for being the go-to problem solver, the organiser of all things, producing high standards of work even under pressure. I’m also a confident communicator, and I understand that you’re busy running your business.

Target Market(s)

Small to Medium Business who require assistance in their business by a virtual assistant.

Industry/Entity Type

Virtual Assistant

Contact Information for Business Card

Mobile: 61 487 902 346

Font styles to use
Sans Serif

Colors
ffffff

Requirements
Must have
• Branding Colours as outlined.
Contact Details as outlined.
Logo as provided.
Proper contact details - mobile, facebook, instragm, website.
Simple, Elegant, very clean looking.
Should not have
• Note cute with pictures.
Not too girly as still want to market to construction companies.

```html
<!DOCTYPE html>
<html lang="en">
<head>
<meta charset="utf-8">
<title>RW Office Partners – Business Card</title>
<link rel="stylesheet" href="https://fonts.googleapis.com/css2?family=Arimo:wght@400;500&display=swap">
<style>
  :root {
    --mauve: #986474;
    --slate: #7a8498;
    --white: #ffffff;
  }
  * { margin: 0; padding: 0; box-sizing: border-box; }
  html, body { width: 1200px; height: 749px; overflow: hidden; background: var(--white); }
  .card {
    position: relative;
    width: 1200px;
    height: 749px;
    overflow: hidden;
    font-family: "Arimo", Arial, sans-serif;
    background: var(--mauve);
  }
  .card__backdrop { position: absolute; inset: 0; }
  .contact-row {
    position: absolute;
    left: 0;
    height: 70px;
    display: flex;
    align-items: center;
  }
  .contact-row__tab {
    position: relative;
    width: 156px;
    height: 70px;
    background: var(--slate);
    flex: none;
  }
  .contact-row__tab::before {
    content: "";
    position: absolute;
    left: 0; top: 0;
    width: 156px; height: 62px;
    background: var(--mauve);
  }
  .contact-row__icon {
    position: absolute;
    right: 10px;
    top: 31px;
    transform: translateY(-50%);
  }
  .contact-row__text {
    margin-left: 10px;
    margin-top: -8px;
    font-size: 26px;
    color: var(--slate);
    letter-spacing: 0.2px;
  }
  .row-email { top: 238px; }
  .row-phone { top: 338px; }
  .row-web { top: 438px; }
  .social {
    position: absolute;
    top: 634px;
    display: flex;
    align-items: center;
    gap: 6px;
    font-size: 19px;
    color: var(--slate);
  }
  .social__dot {
    width: 14px; height: 14px;
    border-radius: 50%;
    background: var(--mauve);
  }
  .social--facebook { left: 88px; }
  .social--instagram { left: 370px; }
  .brand-name {
    position: absolute;
    left: 715px;
    top: 350px;
    font-size: 42px;
    font-weight: 500;
    color: var(--white);
    letter-spacing: 0.5px;
  }
</style>
</head>
<body>
<main class="card">
  <svg class="card__backdrop" width="1200" height="749" viewBox="0 0 1200 749" aria-hidden="true">
    <path fill="var(--slate)" d="M0,0 H582 Q790,375 578,749 H0 Z"/>
    <path fill="var(--white)" d="M0,0 H548 Q820,375 545,749 H0 Z"/>
  </svg>

  <div class="contact-row row-email">
    <div class="contact-row__tab">
      <svg class="contact-row__icon" width="46" height="32" viewBox="0 0 46 32" aria-hidden="true">
        <rect x="1" y="1" width="44" height="30" fill="var(--white)"/>
        <path d="M1,1 L23,18 L45,1" fill="none" stroke="var(--mauve)" stroke-width="2.5"/>
        <path d="M1,31 L17,14 M45,31 L29,14" fill="none" stroke="var(--mauve)" stroke-width="2"/>
      </svg>
    </div>
    <span class="contact-row__text">marisol@rwofficepartners.com.au</span>
  </div>

  <div class="contact-row row-phone">
    <div class="contact-row__tab">
      <svg class="contact-row__icon" width="28" height="46" viewBox="0 0 28 46" aria-hidden="true" style="right:14px">
        <rect x="1" y="1" width="26" height="44" rx="4" fill="var(--white)"/>
        <rect x="4" y="7" width="20" height="29" fill="var(--mauve)"/>
        <circle cx="14" cy="40.5" r="2" fill="var(--mauve)"/>
      </svg>
    </div>
    <span class="contact-row__text">61 487 902 346</span>
  </div>

  <div class="contact-row row-web">
    <div class="contact-row__tab">
      <svg class="contact-row__icon" width="38" height="38" viewBox="0 0 38 38" aria-hidden="true" style="right:12px">
        <circle cx="19" cy="19" r="17" fill="var(--white)"/>
        <g fill="none" stroke="var(--mauve)" stroke-width="2">
          <ellipse cx="19" cy="19" rx="7" ry="17"/>
          <line x1="19" y1="2" x2="19" y2="36"/>
          <line x1="2" y1="19" x2="36" y2="19"/>
          <path d="M5,10 H33 M5,28 H33"/>
        </g>
        <path d="M24,23 L35,28 L30,30 L28,35 Z" fill="var(--white)" stroke="var(--mauve)" stroke-width="1.5"/>
      </svg>
    </div>
    <span class="contact-row__text">www.rwofficepartners.com.au</span>
  </div>

  <div class="social social--facebook">
    <span class="social__dot"></span>
    <span>@rwofficepartners</span>
  </div>
  <div class="social social--instagram">
    <span class="social__dot"></span>
    <span>@rwofficepartners</span>
  </div>

  <p class="brand-name">RW Office Partners</p>
</main>
</body>
</html>
```